BRX Lakeshore Golf Tournament

Need a flyer/poster design that stands out and intrigues people to attend our golf tournament. Flyer will need to be of print quality, high res, able to be resized as we may use it for a postcard as well. The tournament is held at a 5 star golf course and is of a higher caliber/clientele, mostly male M&A professionals. I would like the flyer to reflect our venue and audience.

Balance of masculine and feminine
More contemporary than conservative
Balance of fun and professional
Bold over traditional

I included two sample flyers that are very different but well done in my opinion.
I prefer multiple uses of fonts, sizes to create visual interest

BRX Pactwrights logo (this is also tournament name) colors are similar to logo- I like to accent with an aqua because it gives off a clean look
Info: 11th Annual Golf Tournament, Harrowmere Country Club, November 10th
Schedule: Lunch at 11am, Shotgun at noon, Awards Dinner at 5:30pm
Pricing: $175 per player includes one raffle ticket
Register by Wednesday, November 5th www.brxnet-example.org/lks/events
Use the picture of Harrowmere CC if it works
Young Fairway is our charity partner, please use logo
Near bottom, "Sponsorship Opportunities Available"

```html
<!DOCTYPE html>
<html lang="en">
<head>
<meta charset="utf-8">
<title>BRX Lakeshore Golf Tournament</title>
<link rel="stylesheet" href="https://fonts.googleapis.com/css2?family=Aldrich&family=Lora:wght@500&family=Varela+Round&family=Open+Sans:wght@600;700&display=swap">
<style>
  :root {
    --grass-dark: #2f5a1c;
    --grass: #5e9a2e;
    --sky: #dfeef3;
    --brand-green: #5cb646;
    --deep-green: #1f5a2c;
    --band: #dcecc9;
    --paper: #f3faf9;
    --aqua-soft: #d5efee;
    --yellow: #f3e31a;
    --white: #ffffff;
    --navy: #1b3f8b;
    --ink: #2a2a2a;
  }
  * { margin: 0; padding: 0; box-sizing: border-box; }
  html, body { width: 848px; height: 1200px; overflow: hidden; background: var(--white); }
  .poster {
    position: relative; width: 848px; height: 1200px; overflow: hidden;
    background: linear-gradient(180deg, var(--paper) 0%, var(--aqua-soft) 55%, var(--paper) 100%);
    font-family: "Varela Round", "Open Sans", sans-serif;
  }
  .hero-photo {
    position: absolute; left: 0; top: 0; width: 848px; height: 668px;
    background: linear-gradient(180deg, var(--sky) 0%, #cfe3d8 18%, #7fa94a 34%, var(--grass) 55%, var(--grass-dark) 100%);
  }
  .hero-swoop { position: absolute; left: 0; top: 0; width: 848px; height: 668px; }
  .host-mark {
    position: absolute; left: 580px; top: 110px; width: 240px;
    display: flex; align-items: center; gap: 10px;
    font-size: 22px; color: var(--deep-green); white-space: nowrap;
  }
  .host-mark .dot { width: 18px; height: 18px; border-radius: 50%; background: var(--brand-green); flex: none; }
  .event-date {
    position: absolute; right: 56px; top: 452px; text-align: right;
    font-family: "Open Sans", sans-serif; font-weight: 700; font-size: 44px; line-height: 44px;
    color: var(--yellow);
  }
  .date-rule { position: absolute; left: 790px; top: 432px; }
  .title-annual {
    position: absolute; left: 14px; top: 596px; color: var(--white);
    font-family: "Aldrich", sans-serif; font-weight: 400; font-size: 80px; line-height: 80px; letter-spacing: 7px;
    white-space: nowrap;
  }
  .title-annual .ordinal { font-family: "Lora", serif; font-weight: 500; font-size: 90px; letter-spacing: -3px; margin-right: 18px; }
  .title-golf {
    position: absolute; left: 46px; top: 674px; display: flex; align-items: center;
    font-family: "Aldrich", sans-serif; font-weight: 400; font-size: 108px; line-height: 100px; color: var(--brand-green);
  }
  .golf-ball {
    width: 90px; height: 90px; border-radius: 50%; margin: 0 2px;
    background: radial-gradient(circle at 35% 30%, #ffffff 0%, #e4e4e4 55%, #9a9a9a 100%);
  }
  .title-tournament {
    position: absolute; left: 46px; top: 760px;
    font-family: "Aldrich", sans-serif; font-weight: 400; font-size: 84px; line-height: 80px; letter-spacing: 1px;
    color: var(--brand-green); white-space: nowrap;
  }
  .venue {
    position: absolute; left: 58px; top: 832px; white-space: nowrap;
    font-family: "Open Sans", sans-serif; font-weight: 600; font-size: 34px; color: var(--deep-green);
  }
  .info-band {
    position: absolute; left: 0; top: 880px; width: 848px; height: 122px;
    background: var(--band);
  }
  .schedule {
    position: absolute; left: 62px; top: 896px; font-size: 26px; line-height: 33px; color: var(--deep-green);
    white-space: nowrap;
  }
  .schedule .second { font-size: 23px; }
  .divider { position: absolute; width: 2px; background: var(--deep-green); }
  .divider.info { left: 436px; top: 890px; height: 104px; }
  .divider.price { left: 292px; top: 1014px; height: 56px; }
  .register {
    position: absolute; left: 456px; top: 898px; font-size: 25px; line-height: 32px; color: var(--deep-green);
    white-space: nowrap;
  }
  .register .lead { color: var(--brand-green); }
  .register .url { font-size: 20px; }
  .price {
    position: absolute; top: 1014px; color: var(--deep-green); font-size: 28px; line-height: 32px; white-space: nowrap;
  }
  .price small { font-size: 22px; color: var(--brand-green); }
  .price .note { display: block; font-size: 16px; line-height: 22px; color: var(--ink); }
  .price.single { left: 62px; }
  .price.team { left: 314px; }
  .sponsorship { position: absolute; left: 10px; top: 1158px; font-size: 17px; color: var(--ink); white-space: nowrap; }
  .partner-label { position: absolute; left: 488px; top: 1157px; font-size: 18px; color: var(--ink); white-space: nowrap; }
  .partner-mark {
    position: absolute; left: 664px; top: 1074px; width: 180px;
    display: flex; flex-direction: column; align-items: center; gap: 6px;
    font-size: 22px; line-height: 26px; color: var(--navy); text-align: center; white-space: nowrap;
  }
  .partner-mark .dot { width: 26px; height: 26px; border-radius: 50%; background: var(--navy); }
</style>
</head>
<body>
<main class="poster">
  <div class="hero-photo" role="img" aria-label="Close-up of a gloved hand placing a golf ball on a tee beside an iron club on green fairway grass"></div>
  <svg class="hero-swoop" viewBox="0 0 848 668" aria-hidden="true">
    <path d="M0 0 L40 0 C40 300 250 560 650 668 L0 668 Z" fill="#7fae3a" opacity="0.55"/>
    <path d="M0 30 C60 330 290 580 640 668" fill="none" stroke="#e7ec7a" stroke-width="3" opacity="0.7"/>
  </svg>

  <div class="host-mark"><span class="dot"></span>BRX Pactwrights</div>

  <div class="event-date">November<br>10th</div>
  <svg class="date-rule" width="30" height="110" aria-hidden="true"><line x1="26" y1="2" x2="4" y2="108" stroke="#f3e31a" stroke-width="3"/></svg>

  <h1>
    <span class="title-annual"><span class="ordinal">11th</span>ANNUAL</span>
    <span class="title-golf">G<span class="golf-ball" role="img" aria-label="Golf ball"></span>LF</span>
    <span class="title-tournament">TOURNAMENT</span>
  </h1>
  <p class="venue">Harrowmere Country Club</p>

  <div class="info-band"></div>
  <p class="schedule">Lunch at 11am,<br><span class="second">Shotgun at noon,</span><br>Awards Dinner at 5:30pm</p>
  <span class="divider info"></span>
  <p class="register"><span class="lead">Register by Wednesday</span><br>November 5th<br><span class="url">www.brxnet-example.org/lks/events</span></p>

  <p class="price single">$175 <small>per player</small><span class="note">Includes one raffle ticket</span></p>
  <span class="divider price"></span>
  <p class="price team">$700 <small>for 4 players</small><span class="note">Includes four raffle ticket</span></p>

  <p class="sponsorship">"Sponsorship Opportunities Available"</p>
  <p class="partner-label">Charity Partner</p>
  <div class="partner-mark"><span class="dot"></span><span>Young Fairway<br>Greater Dallas</span></div>
</main>
</body>
</html>
```